Demolition Company Billboard Design 13 feet wide 15 feet high

This is my first billboard on a busy road. I want it to be professional but with some eye catching flair that matches by business which is a demoltion business and also list my services. My company slogan is also

"call hollick, watch it fall"

Target Market(s)

Home Ownerd and General Construction Companies

Industry/Entity Type

construction

Colors
0054AA
0677BA
7BADD7
CADEEF
E8F1F8

Requirements
Must have
• My services listed in the pictures my website and my phone number

```html
<!DOCTYPE html>
<html lang="en">
<head>
<meta charset="utf-8">
<title>Hollick Demolition Billboard</title>
<link href="https://fonts.googleapis.com/css2?family=Barlow:wght@600;700;800&family=Montserrat:wght@600&display=swap" rel="stylesheet">
<style>
  :root {
    --stage: #4d4d4d;
    --caption: #b5b5b5;
    --white: #ffffff;
    --royal: #1257b0;
    --royal-light: #2a6bc0;
    --slate: #474747;
    --hatch: #6a6a6a;
    --navy: #0d1f45;
    --ice: #cadeef;
    --link: #0054aa;
    --logo-ink: #444444;
    --logo-frame: #1f4d7d;
  }
  * { margin: 0; padding: 0; box-sizing: border-box; }
  html, body { width: 1040px; height: 1200px; overflow: hidden; background: var(--stage); }
  .stage { position: relative; width: 1040px; height: 1200px; }
  .caption {
    position: absolute; top: 80px; left: 0; width: 100%;
    text-align: center; color: var(--caption);
    font: 600 29px/36px "Montserrat", sans-serif; letter-spacing: 0.5px;
  }
  .billboard { position: absolute; left: 132px; top: 208px; width: 777px; height: 897px; background: var(--white); overflow: hidden; }
  .billboard svg { display: block; }
  .headline { font-family: "Barlow", sans-serif; font-weight: 800; }
  .headline .light { fill: var(--ice); }
  .headline .bright { fill: var(--white); }
  .brand-name { font: 700 54px "Barlow", sans-serif; fill: var(--logo-ink); letter-spacing: 3px; }
  .services-title { font: 700 31px "Barlow", sans-serif; fill: var(--ice); }
  .service-item { font: 700 22px "Barlow", sans-serif; fill: var(--white); }
  .chevron { fill: none; stroke: var(--white); stroke-width: 3; }
  .phone { font: 800 62px "Barlow", sans-serif; fill: var(--navy); }
  .website { font: 800 30px "Barlow", sans-serif; fill: var(--link); }
</style>
</head>
<body>
<div class="stage">
  <p class="caption">Demolition Company Billboard Design<br>13 feet wide 15 feet high</p>

  <div class="billboard">
    <svg width="777" height="897" viewBox="0 0 777 897" xmlns="http://www.w3.org/2000/svg">
      <defs>
        <linearGradient id="siteTone" x1="0" y1="0" x2="1" y2="1">
          <stop offset="0" stop-color="#1c1c1c"/>
          <stop offset="0.45" stop-color="#3a3330"/>
          <stop offset="0.75" stop-color="#5b4538"/>
          <stop offset="1" stop-color="#2a2522"/>
        </linearGradient>
        <linearGradient id="interiorTone" x1="0" y1="0" x2="1" y2="1">
          <stop offset="0" stop-color="#8b8770"/>
          <stop offset="0.5" stop-color="#a59f8e"/>
          <stop offset="1" stop-color="#6f6a60"/>
        </linearGradient>
      </defs>

      <!-- site photo band -->
      <rect class="site-photo" x="0" y="197" width="777" height="600" fill="url(#siteTone)" role="img" aria-label="Photo of an excavator demolishing an old brick building"/>

      <!-- top corner blue sweep -->
      <path class="corner-sweep" d="M414 0 H777 V248 Q660 250 605 193 Z" fill="var(--royal)"/>
      <path d="M470 0 H520 L720 200 Q700 205 680 200 Z" fill="var(--royal-light)" opacity="0.5"/>
      <path d="M560 0 H610 L777 160 V205 Z" fill="var(--royal-light)" opacity="0.45"/>
      <path d="M660 0 H700 L777 75 V115 Z" fill="var(--royal-light)" opacity="0.4"/>

      <!-- white header -->
      <path class="header" d="M0 0 H414 L492 81 L377 197 H0 Z" fill="var(--white)"/>

      <!-- slate triangle with hatching -->
      <path class="slate-wedge" d="M492 81 L605 193 L586 197 H377 Z" fill="var(--slate)"/>
      <g class="hatching" fill="var(--hatch)">
        <path d="M413 164 H429 L410 187 H394 Z"/>
        <path d="M445 164 H461 L442 187 H426 Z"/>
        <path d="M477 164 H493 L474 187 H458 Z"/>
        <path d="M509 164 H525 L506 187 H490 Z"/>
        <path d="M541 164 H557 L538 187 H522 Z"/>
      </g>

      <!-- brand -->
      <rect class="brand-square" x="82" y="82" width="40" height="40" fill="var(--logo-frame)"/>
      <text class="brand-name" x="136" y="122">HOLLICK</text>

      <!-- headline -->
      <text class="headline light" x="54" y="349" font-size="128">CALL</text>
      <text class="headline bright" x="54" y="434" font-size="80">HOLLICK,</text>
      <text class="headline bright" x="56" y="500" font-size="64">WATCH IT</text>
      <text class="headline light" x="54" y="602" font-size="124">FALL</text>

      <!-- lower white field -->
      <path class="footer" d="M0 779 H460 L415 690 Q440 680 480 680 H700 Q740 680 777 700 V897 H0 Z" fill="var(--white)"/>

      <!-- lower left blue sweep -->
      <path class="base-sweep" d="M0 645 Q40 640 70 665 L183 779 H0 Z" fill="var(--royal)"/>
      <path d="M0 700 L79 779 H40 L0 740 Z" fill="var(--royal-light)" opacity="0.5"/>
      <path class="base-band" d="M70 665 Q85 680 100 690 L183 779 H163 L58 674 Z" fill="var(--slate)"/>
      <path d="M60 680 L165 779 H215 L100 664 Z" fill="var(--slate)"/>

      <!-- inset photo -->
      <path d="M56 649 H326 L455 791 H198 Z" fill="var(--white)"/>
      <path class="inset-photo" d="M75 656 H317 L436 785 H207 Z" fill="url(#interiorTone)" role="img" aria-label="Photo of an excavator bucket clearing a gutted industrial interior"/>

      <!-- services panel -->
      <rect class="services" x="472" y="637" width="271" height="241" fill="var(--navy)"/>
      <text class="services-title" x="493" y="680">OUR SERVICES</text>
      <g class="service-list">
        <path class="chevron" d="M497 696 L504 704 L497 712"/><text class="service-item" x="516" y="712">Room Gut Out</text>
        <path class="chevron" d="M497 725 L504 733 L497 741"/><text class="service-item" x="516" y="741">House Gut Out</text>
        <path class="chevron" d="M497 754 L504 762 L497 770"/><text class="service-item" x="516" y="770">Partial Demolition</text>
        <path class="chevron" d="M497 783 L504 791 L497 799"/><text class="service-item" x="516" y="799">Full Demolition</text>
        <path class="chevron" d="M497 812 L504 820 L497 828"/><text class="service-item" x="516" y="828">Commercial</text>
        <path class="chevron" d="M497 841 L504 849 L497 857"/><text class="service-item" x="516" y="857">Residential</text>
      </g>

      <!-- contact -->
      <text class="phone" x="54" y="837" textLength="386" lengthAdjust="spacingAndGlyphs">(412) 555-0148</text>
      <text class="website" x="61" y="876" textLength="378" lengthAdjust="spacingAndGlyphs">www.hollickdemolition.com</text>
    </svg>
  </div>
</div>
</body>
</html>
```